Motivational Poster Design Project

I would like to create a poster with some of my favorite quotes to hang in my office. I did a similar project in 2012 and I've uploaded the top 2 designs so you can get a better idea of what I'm looking for. I will provide feedback on your design within 24 hours of receiving it.

The poster must contain the following quotes:

"You’re only given a little spark of madness. You mustn’t lose it.”
- Dorian Halbrook

“The most contrarian thing of all is not to oppose the crowd but to think for yourself.”
- Marcus Vell

"I constantly see people rise in life who are not the smartest, sometimes not even the most diligent, but they are learning machines. They go to bed every night a little wiser than they were when they got up and boy does that help, particularly when you have a long run ahead of you."
- Walter Brisco

“In theory, there’s no difference between theory and practice. But, in practice, there is.”
- Piet R. K. Ter Wolvenkamp

"At the end of the day, a reactionary life is a normal life. One thing is consistent in every remarkable person: they decide to do something remarkable. Don’t let the world choose who you become."
- Ravindra Kolpe

“It usually takes 3-4 months to try enough that you can do a proper 80/20 analysis, then two months to design systems to scale what *is* working.”
-Gus Ambery

“Authority is 20 percent given, 80 percent taken.”
- Harold Quimsby

“Your actions are consistent with the way the world occurs to you.”
- Anselm Grottke

Project Deadline Extended
Reason: I am going to be travelling with no access to internet until January 5th, 2015. I am extending the project deadline until 12/31/14 and I'll make a final decision during the 1st week of January.

Target Market(s)

Personal Project

Industry/Entity Type

Learning

Requirements
Must have
• The poster will be 24" high x 36" long and printed on canvas, so the image you create needs to have a resolution of at least 2700 x 3900.
Nice to have
• I don't have an exact vision for how the poster should look, so I am totally open to you using your creativity to develop, arrange and present the content as you'd like.
• That said, I would like an image (photo or posterized image) of the person being quoted along with each quote. I do not have specific images that I would like you to use, so you will need to find the images on your own. The images don't need to be perfect... I am more interested in the poster relating the essence of the quotes and the people being quoted than I am in perfect photographic images of the people being quoted.

```html
<!DOCTYPE html>
<html lang="en">
<head>
<meta charset="utf-8">
<title>Eight Quotes – Learning Poster</title>
<link rel="stylesheet" href="https://fonts.googleapis.com/css2?family=Tinos:wght@400;700&display=swap">
<style>
  :root {
    --bg-center: #3b332d;
    --bg-mid: #241f1b;
    --bg-edge: #0b0a09;
    --quote-text: #f3efe9;
    --numeral: #7a746e;
    --portrait-light: #9a938b;
    --portrait-dark: #4a433d;
    --name-pink: #f2a7cf;
    --name-blue: #a9cdf0;
    --name-gold: #f1e4a6;
    --name-lilac: #c9c2f2;
  }
  html, body { margin: 0; padding: 0; overflow: hidden; background: var(--bg-edge); }
  .poster {
    position: relative;
    width: 800px;
    height: 1200px;
    overflow: hidden;
    font-family: "Tinos", "Times New Roman", serif;
    color: var(--quote-text);
    background:
      repeating-linear-gradient(90deg, rgba(255,255,255,0.012) 0 2px, rgba(0,0,0,0.03) 2px 5px),
      radial-gradient(ellipse 62% 55% at 50% 48%, var(--bg-center) 0%, var(--bg-mid) 55%, var(--bg-edge) 100%);
  }
  .portrait {
    position: absolute;
    border-radius: 50%;
    background: radial-gradient(ellipse at 50% 45%, var(--portrait-light) 0%, var(--portrait-dark) 45%, rgba(40,35,31,0) 72%);
  }
  .numeral {
    position: absolute;
    margin: 0;
    color: var(--numeral);
    font-weight: 400;
    line-height: 1;
  }
  .quote {
    position: absolute;
    margin: 0;
    text-align: center;
    font-size: 15px;
    line-height: 27px;
  }
  .quote p { margin: 0; }
  .quote strong { font-size: 21px; font-weight: 700; }
  .quote cite {
    display: block;
    font-style: normal;
    font-size: 13px;
    line-height: 30px;
  }
  .pink { color: var(--name-pink); }
  .blue { color: var(--name-blue); }
  .gold { color: var(--name-gold); }
  .lilac { color: var(--name-lilac); }
  .still-life {
    position: absolute;
    background: radial-gradient(ellipse at 50% 50%, rgba(120,112,104,0.45) 0%, rgba(40,35,31,0) 70%);
  }
</style>
</head>
<body>
<main class="poster">

  <div class="portrait" style="left:96px;top:100px;width:96px;height:100px" role="img" aria-label="Portrait of Dorian Halbrook"></div>
  <div class="portrait" style="left:594px;top:132px;width:114px;height:162px" role="img" aria-label="Portrait of Marcus Vell speaking at a podium"></div>
  <div class="portrait" style="left:48px;top:294px;width:108px;height:156px" role="img" aria-label="Portrait of Walter Brisco"></div>
  <div class="portrait" style="left:570px;top:498px;width:126px;height:120px" role="img" aria-label="Portrait of Piet R. K. Ter Wolvenkamp"></div>
  <div class="portrait" style="left:48px;top:564px;width:144px;height:144px" role="img" aria-label="Portrait of Ravindra Kolpe"></div>
  <div class="portrait" style="left:606px;top:720px;width:102px;height:120px" role="img" aria-label="Portrait of Gus Ambery"></div>
  <div class="portrait" style="left:72px;top:816px;width:120px;height:156px" role="img" aria-label="Portrait of Harold Quimsby"></div>
  <div class="portrait" style="left:678px;top:882px;width:90px;height:138px" role="img" aria-label="Portrait of Anselm Grottke"></div>

  <div class="still-life" style="left:110px;top:1040px;width:450px;height:110px" role="img" aria-label="Quill pen lying across the foot of the poster"></div>
  <div class="still-life" style="left:690px;top:1070px;width:110px;height:110px" role="img" aria-label="Ink pot"></div>

  <p class="numeral" style="left:528px;top:96px;font-size:84px">1</p>
  <p class="numeral" style="left:186px;top:278px;font-size:58px">2</p>
  <p class="numeral" style="left:616px;top:356px;font-size:92px">3</p>
  <p class="numeral" style="left:154px;top:534px;font-size:88px">4</p>
  <p class="numeral" style="left:616px;top:646px;font-size:66px">5</p>
  <p class="numeral" style="left:196px;top:764px;font-size:64px">6</p>
  <p class="numeral" style="left:544px;top:884px;font-size:86px">7</p>
  <p class="numeral" style="left:442px;top:1040px;font-size:72px">8</p>

  <blockquote class="quote" style="left:184px;top:138px;width:400px">
    <p>“You’re only given a little <strong>spark</strong> of madness.<br>You mustn’t <strong>lose</strong> it.”</p>
    <cite class="pink">- Dorian Halbrook</cite>
  </blockquote>

  <blockquote class="quote" style="left:184px;top:252px;width:400px">
    <p>“The most contrarian thing of all is not to oppose<br>the crowd but to <strong>think for yourself</strong>.”</p>
    <cite class="blue">- Marcus Vell</cite>
  </blockquote>

  <blockquote class="quote" style="left:90px;top:362px;width:620px">
    <p>“I constantly see people rise in life who are not the smartest, sometimes<br>not even the most diligent, but they are learning machines.<br>They go to bed every night a little wiser than they were when they got up<br>and boy does that help, particularly when you have a <strong>long run ahead</strong> of you.”</p>
    <cite class="gold">- Walter Brisco</cite>
  </blockquote>

  <blockquote class="quote" style="left:184px;top:529px;width:400px">
    <p>“In theory, there’s no between theory and practice.<br>But, in <strong>practice</strong>, there is.”</p>
    <cite class="lilac">- Piet R. K. Ter Wolvenkamp</cite>
  </blockquote>

  <blockquote class="quote" style="left:124px;top:642px;width:520px">
    <p>“At the end of the day, a reactionary life is a normal life. One thing is<br>consistent in every remarkable person : they decide to do something<br>remarkable. <strong>Don’t let the world choose who you become</strong>.”</p>
    <cite class="pink">- Ravindra Kolpe</cite>
  </blockquote>

  <blockquote class="quote" style="left:172px;top:780px;width:400px">
    <p>“It usually takes 3-4 months to try enough<br>that you can do a proper 80/20 analysis, then two months<br>to design systems to scale <strong>what *is* working</strong>.”</p>
    <cite class="blue">- Gus Ambery</cite>
  </blockquote>

  <blockquote class="quote" style="left:184px;top:916px;width:400px">
    <p>“Authority is 20 percent <strong>given</strong>, 80 percent <strong>taken</strong>.”</p>
    <cite class="gold">- Harold Quimsby</cite>
  </blockquote>

  <blockquote class="quote" style="left:134px;top:1002px;width:500px">
    <p>“Your actions are <strong>consistent</strong> with the way the world occurs to you.”</p>
    <cite class="blue">- Anselm Grottke</cite>
  </blockquote>

</main>
</body>
</html>
```